dirty dancer in bathtub promotion

Need graphics for side of bathtub for a party -event promotion ( as shown in photo below). graphics must be contained in an area of 38” x 15” for entire name.
Company name that will be written across the tub is
MERIDIAN TILEWORK COLLECTIVE The theme event is Art Deco so font should be in an Art Deco like font and SEXY

Target Market(s)

Architects and designers

Font styles to use
Other font styles liked:
• Art Deco

Colors
ffffff
edf7f6

Requirements
Must have
• Professional - creative white lettering
Nice to have
• Art Deco font MUST BE ALL WHITE...(as bathtub is dark copper color )

```html
<!DOCTYPE html>
<html lang="en">
<head>
<meta charset="utf-8">
<title>Meridian Tilework Collective – Tub Graphic 38 x 15</title>
<link rel="stylesheet" href="https://fonts.googleapis.com/css2?family=Limelight&family=PT+Sans&display=swap">
<style>
  :root {
    --stage-light: #b9b9b9;
    --stage-dark: #3a3a3a;
    --panel: #000000;
    --frame: #9a5496;
    --lettering: #ffffff;
    --label: #1a1a1a;
    --photo-violet: #5e3468;
    --photo-amber: #8a4a1c;
    --photo-deep: #1a0c16;
  }
  * { margin: 0; padding: 0; box-sizing: border-box; }
  html, body { width: 1200px; height: 1000px; overflow: hidden; }
  body {
    position: relative;
    background: linear-gradient(to bottom, var(--stage-dark) 0%, var(--stage-light) 50%, var(--stage-dark) 100%);
    font-family: "PT Sans", sans-serif;
  }
  .size-label {
    position: absolute;
    left: 77px;
    top: 247px;
    font-size: 25px;
    color: var(--label);
    letter-spacing: 0.5px;
  }
  .tub-panel {
    position: absolute;
    left: 56px;
    top: 286px;
    width: 1094px;
    height: 432px;
    background: var(--panel);
    overflow: hidden;
  }
  .event-photo {
    position: absolute;
    left: 160px;
    top: 38px;
    width: 900px;
    height: 356px;
    background:
      radial-gradient(ellipse 30% 45% at 65% 35%, rgba(214,170,200,0.55), transparent 70%),
      radial-gradient(ellipse 35% 25% at 64% 78%, rgba(190,120,190,0.7), transparent 75%),
      radial-gradient(ellipse 30% 30% at 40% 80%, rgba(138,74,28,0.6), transparent 75%),
      linear-gradient(to right, var(--panel) 0%, var(--photo-deep) 35%, var(--photo-violet) 70%, var(--photo-amber) 100%);
  }
  .frame {
    position: absolute;
    inset: 0;
  }
  .company-name {
    position: absolute;
    left: 82px;
    top: 84px;
    font-family: "Limelight", serif;
    font-weight: 400;
    font-size: 64px;
    line-height: 84px;
    color: var(--lettering);
    letter-spacing: 1px;
    text-transform: uppercase;
  }
  .company-name span { display: block; }
</style>
</head>
<body>
  <div class="size-label">38″ x 15″</div>

  <section class="tub-panel">
    <div class="event-photo" role="img" aria-label="Party photo of a dancer standing in a clawfoot bathtub showered with gold confetti, guests and warm bokeh lights behind"></div>

    <svg class="frame" width="1094" height="432" viewBox="0 0 1094 432" fill="none" stroke="var(--frame)" stroke-width="2">
      <!-- horizontal rules -->
      <line x1="101" y1="30" x2="997" y2="30"/>
      <line x1="101" y1="402" x2="997" y2="402"/>
      <!-- vertical rules -->
      <line x1="32" y1="98" x2="32" y2="334"/>
      <line x1="1062" y1="98" x2="1062" y2="334"/>
      <!-- corner: top left -->
      <rect x="22" y="20" width="18" height="18"/>
      <rect x="30" y="28" width="18" height="18"/>
      <line x1="40" y1="20" x2="101" y2="20"/>
      <line x1="22" y1="38" x2="22" y2="98"/>
      <!-- corner: top right -->
      <rect x="1054" y="20" width="18" height="18"/>
      <rect x="1046" y="28" width="18" height="18"/>
      <line x1="993" y1="20" x2="1054" y2="20"/>
      <line x1="1072" y1="38" x2="1072" y2="98"/>
      <!-- corner: bottom left -->
      <rect x="22" y="394" width="18" height="18"/>
      <rect x="30" y="386" width="18" height="18"/>
      <line x1="40" y1="412" x2="101" y2="412"/>
      <line x1="22" y1="334" x2="22" y2="394"/>
      <!-- corner: bottom right -->
      <rect x="1054" y="394" width="18" height="18"/>
      <rect x="1046" y="386" width="18" height="18"/>
      <line x1="993" y1="412" x2="1054" y2="412"/>
      <line x1="1072" y1="334" x2="1072" y2="394"/>
    </svg>

    <h1 class="company-name">
      <span>Meridian</span>
      <span>Tilework</span>
      <span>Collective</span>
    </h1>
  </section>
</body>
</html>
```